Business Card front and back

I am looking for business card design. I really really like the design file I uploaded named 627788_19250069_3478263_85f427ee_image

Target Market(s)

Corporate Fitness High end Private country club

Industry/Entity Type

Fitness Industry

Contact Information for Business Card

The last image I like as an example I uploaded a bunch of my logos. The file labeled "the signature" is my business card information for you to use

Colors
0054AA
0677BA
7BADD7
CADEEF
E8F1F8

Requirements
Must have
• E-mail sigThe file I uploaded labeled "627788_19250069_3478263_85f427ee_image" with all the plus signs on the back if those could be the logo symbol I uploaded labeled "1 back.png"

```html
<!DOCTYPE html>
<html lang="en">
<head>
<meta charset="utf-8">
<title>Stride Works – Business Card</title>
<link rel="stylesheet" href="https://fonts.googleapis.com/css2?family=Arimo&family=Montserrat:wght@400;600&display=swap">
<style>
  :root {
    --stage: #4d4d4d;
    --card: #202020;
    --card-edge: #161616;
    --blue: #1f82c8;
    --white: #ffffff;
    --pattern-dark: #161616;
    --pattern-light: #6a6a6a;
  }
  * { box-sizing: border-box; margin: 0; padding: 0; }
  html, body { width: 1200px; height: 1200px; overflow: hidden; }
  body { background: var(--stage); position: relative; font-family: "Montserrat", sans-serif; }

  .card {
    position: absolute;
    width: 942px;
    height: 505px;
    background: var(--card);
    border: 1px solid var(--card-edge);
    overflow: hidden;
  }
  .card--front { left: 131px; top: 64px; }
  .card--back { left: 127px; top: 632px; }

  .front-pattern {
    position: absolute; inset: 0;
    background: linear-gradient(200deg, var(--pattern-light) 0%, #2c2c2c 38%, var(--pattern-dark) 70%, #1c1c1c 100%);
  }
  .brand {
    position: absolute;
    left: 0; right: 0; top: 215px;
    display: flex; align-items: center; justify-content: center; gap: 18px;
  }
  .brand__mark { width: 46px; height: 46px; background: var(--blue); }
  .brand__name {
    font-family: "Montserrat", sans-serif;
    font-weight: 600;
    font-size: 48px;
    letter-spacing: 3px;
    color: var(--white);
    line-height: 1;
  }

  .holder { position: absolute; left: 60px; top: 86px; }
  .holder__name {
    font-family: "Arimo", sans-serif;
    font-weight: 400;
    font-size: 54px;
    color: var(--blue);
    line-height: 1;
    white-space: nowrap;
  }
  .holder__role {
    font-family: "Arimo", sans-serif;
    font-size: 33px;
    color: var(--white);
    margin: 8px 0 0 5px;
    line-height: 1;
  }
  .contact {
    position: absolute; left: 64px; top: 240px;
    list-style: none;
    font-size: 34px;
    color: var(--white);
    white-space: nowrap;
  }
  .contact li { height: 52px; line-height: 40px; }
  .contact .accent { color: var(--blue); }
  .contact .regions { font-family: "Arimo", sans-serif; font-size: 32px; }

  .back-emblem {
    position: absolute;
    left: 505px; top: 103px; width: 392px; height: 296px;
    border-radius: 6px 60px 60px 6px;
    background: linear-gradient(215deg, #6e6e6e 0%, #2a2a2a 35%, #0c0c0c 75%, #050505 100%);
  }
</style>
</head>
<body>
  <section class="card card--front">
    <div class="front-pattern" role="img" aria-label="Repeating brand symbol pattern fading from dark to light grey"></div>
    <div class="brand">
      <span class="brand__mark"></span>
      <span class="brand__name">STRIDE WORKS</span>
    </div>
  </section>

  <section class="card card--back">
    <div class="holder">
      <h1 class="holder__name">DALE MORROW</h1>
      <p class="holder__role">CONSULTANT</p>
    </div>
    <ul class="contact">
      <li>Dale@strideworks.co</li>
      <li>www.<span class="accent">strideworks</span>.co</li>
      <li class="accent">555-214-3870</li>
      <li class="regions">ND. SD. MN. NE. IA. KS</li>
    </ul>
    <div class="back-emblem" role="img" aria-label="Large embossed brand symbol in dark grey gradient"></div>
  </section>
</body>
</html>
```